Whimsical Flyer for Children's Storytime at Lark And Lantern

Design an 8 1/2 by 11 color flyer to promote a storytime series at our store. At Lark And Lantern we believe that the shortest distance between two people is a story. Everything in our store has a story behind it and now we are excited to have one of the world’s best storytellers coming to share her gifts with kids ages 2-5, once a week, starting at 10am on July 7th for an eight-week series. Ms. Dolores (Pettigrew), children’s librarian and storyteller extraordinaire, and our own Mr. Bertram, her budding apprentice, will regale children with music, stories and movement, FREE! 10am. Reservations required. Visit larkandlantern.example for details. 387 E. 61st Avenue - San Mateo CA 94471.

Target Market(s)

Parents and caregivers with children

Requirements
Must have
• Whimsy, fun, enticing to parents and children

```html
<!DOCTYPE html>
<html lang="en">
<head>
<meta charset="utf-8">
<title>Storytime at Lark And Lantern</title>
<link href="https://fonts.googleapis.com/css2?family=Poppins:wght@300;400;500;600;700;800&family=Sacramento&display=swap" rel="stylesheet">
<style>
  :root {
    --olive: #83912a;
    --orange: #de6d31;
    --brown: #8a4b22;
    --ink: #5d5d5d;
    --paper: #ffffff;
    --backdrop: #c4c4c4;
  }
  * { box-sizing: border-box; margin: 0; padding: 0; }
  html, body { width: 1200px; height: 1200px; overflow: hidden; }
  body { background: var(--backdrop); font-family: "Poppins", sans-serif; position: relative; }

  .flyer {
    position: absolute; left: 175px; top: 48px;
    width: 850px; height: 1103px;
    background: var(--paper); overflow: hidden;
  }
  .hero-photo {
    position: absolute; left: 0; top: 0; width: 850px; height: 590px;
    background:
      radial-gradient(ellipse 160px 130px at 300px 250px, #e9c3a4 0%, rgba(233,195,164,0) 100%),
      radial-gradient(ellipse 170px 140px at 500px 300px, #f4cf2e 0%, rgba(244,207,46,0) 100%),
      radial-gradient(ellipse 200px 110px at 180px 360px, #5aa6d8 0%, rgba(90,166,216,0) 100%),
      radial-gradient(ellipse 120px 120px at 120px 140px, #f0c2a8 0%, rgba(240,194,168,0) 100%),
      linear-gradient(180deg, #eef2f4 0%, #f4f4f2 70%, #ffffff 100%);
  }
  .brand {
    position: absolute; right: 30px; top: 62px;
    display: flex; align-items: center; gap: 10px;
    font-weight: 600; font-size: 19px; letter-spacing: 1px;
    color: var(--brown); text-transform: uppercase;
  }
  .brand-dot { width: 22px; height: 22px; border-radius: 50%; background: var(--orange); }

  .title { position: absolute; left: 29px; top: 420px; width: 450px; font-weight: 400; }
  .title-script {
    font-family: "Sacramento", cursive; font-weight: 400; font-size: 96px; line-height: 1;
    color: var(--ink); margin-left: 22px;
  }
  .title-main {
    font-weight: 800; font-size: 74px; line-height: 1; letter-spacing: -1px;
    color: var(--olive); margin-top: -22px;
  }
  .divider { position: absolute; left: 488px; top: 455px; width: 1px; height: 110px; background: #d5d5d5; }

  .date-box { position: absolute; left: 515px; top: 455px; width: 306px; }
  .date-start {
    background: var(--olive); color: #fff; height: 35px; border-radius: 6px 6px 0 0;
    font-size: 25px; font-weight: 400; text-align: center; line-height: 36px;
  }
  .date-main {
    background: var(--orange); color: #fff; margin-top: 2px; height: 75px;
    text-align: center; padding-top: 4px;
  }
  .date-day { font-size: 36px; font-weight: 800; line-height: 40px; }
  .date-series { font-size: 19px; font-weight: 400; line-height: 22px; }

  .storyteller-photo {
    position: absolute; left: 0; top: 608px; width: 442px; height: 495px;
    background:
      radial-gradient(ellipse 95px 115px at 140px 160px, #e5b79c 0%, rgba(229,183,156,0) 100%),
      radial-gradient(ellipse 115px 140px at 140px 140px, #6a3a28 0%, rgba(106,58,40,0) 100%),
      radial-gradient(ellipse 120px 130px at 330px 340px, #e9e0a4 0%, rgba(233,224,164,0) 100%),
      linear-gradient(180deg, #f6f1ec 0%, #ece8e4 55%, #dfe2ee 100%);
  }

  .lead { position: absolute; left: 268px; top: 609px; width: 560px; text-align: center; }
  .lead-head { font-size: 27px; font-weight: 800; color: var(--orange); line-height: 34px; }
  .lead-text { font-size: 22px; font-weight: 400; color: var(--ink); line-height: 25px; text-transform: uppercase; }
  .lead-text strong { color: var(--olive); font-weight: 800; }

  .host-card {
    position: absolute; left: 272px; top: 712px; width: 549px; height: 149px;
    background: var(--brown); border-radius: 12px; color: #fff;
  }
  .host-name { position: absolute; left: 37px; top: 16px; font-size: 34px; font-weight: 700; white-space: nowrap; }
  .host-text { position: absolute; left: 191px; top: 66px; font-size: 17px; line-height: 22.5px; font-weight: 400; }
  .host-text strong { font-weight: 700; }

  .white-cut { position: absolute; left: 442px; top: 861px; width: 408px; height: 186px; background: var(--paper); }

  .activities { position: absolute; left: 455px; top: 892px; }
  .activities-head { font-size: 15.5px; font-weight: 700; color: var(--ink); text-transform: uppercase; }
  .activities-list { display: flex; gap: 18px; margin-top: 4px; list-style: none; font-size: 15.5px; color: var(--ink); }
  .activities-list li { display: flex; align-items: center; gap: 5px; }
  .activities-list svg { width: 14px; height: 14px; }

  .free-tag {
    position: absolute; left: 787px; top: 883px; width: 34px; height: 66px;
    background: var(--olive); color: #fff; border-radius: 3px;
    display: flex; align-items: center; justify-content: center;
  }
  .free-tag span { transform: rotate(-90deg); font-size: 16px; font-weight: 800; white-space: nowrap; }

  .reserve-bar {
    position: absolute; left: 455px; top: 971px; width: 366px; height: 32px;
    background: var(--brown); border-radius: 10px 10px 0 0; color: #fff;
    display: flex; align-items: center; justify-content: center; gap: 10px;
    font-size: 16px;
  }
  .reserve-bar svg { width: 20px; height: 20px; }

  .visit {
    position: absolute; right: 29px; top: 1009px;
    white-space: nowrap; text-align: right;
    font-size: 17px; line-height: 24px; color: var(--ink);
  }
  .visit strong { color: var(--brown); font-weight: 700; }

  .address-band { position: absolute; left: 0; top: 1047px; width: 850px; height: 56px; }
  .address-band svg.band { position: absolute; inset: 0; }
  .address {
    position: absolute; left: 420px; top: 0; height: 56px;
    display: flex; align-items: center; gap: 12px; color: #fff; font-size: 17px;
  }
  .address svg { width: 18px; height: 24px; }
</style>
</head>
<body>
  <main class="flyer">
    <div class="hero-photo" role="img" aria-label="Photo of two young children lying on the floor reading a picture book together"></div>

    <div class="brand"><span class="brand-dot"></span>Lark And Lantern</div>

    <h1 class="title">
      <div class="title-script">Welcome to</div>
      <div class="title-main">STORYTIME</div>
    </h1>
    <div class="divider"></div>

    <div class="date-box">
      <div class="date-start">STARTING AT 10AM</div>
      <div class="date-main">
        <div class="date-day">ON JULY 7TH</div>
        <div class="date-series">AN EIGHT-WEEK SERIES</div>
      </div>
    </div>

    <div class="storyteller-photo" role="img" aria-label="Photo of the storyteller smiling and holding up a children's picture book"></div>

    <section class="lead">
      <h2 class="lead-head">THE WORLD’S BEST STORYTELLERS</h2>
      <p class="lead-text">Coming to share her gifts with kids<br><strong>Ages 2-5</strong> once a week</p>
    </section>

    <section class="host-card">
      <div class="host-name">Ms. Dolores (Pettigrew),</div>
      <p class="host-text">children’s librarian and storyteller<br>extraordinaire, and our own<br><strong>Mr. Bertram</strong>, her budding apprentice</p>
    </section>

    <div class="white-cut"></div>

    <section class="activities">
      <p class="activities-head">They will regale children with</p>
      <ul class="activities-list">
        <li><svg viewBox="0 0 14 14"><path d="M1 7.5 L5 11.5 L13 2.5" fill="none" stroke="#de6d31" stroke-width="2.4" stroke-linecap="round" stroke-linejoin="round"/></svg>MUSIC</li>
        <li><svg viewBox="0 0 14 14"><path d="M1 7.5 L5 11.5 L13 2.5" fill="none" stroke="#de6d31" stroke-width="2.4" stroke-linecap="round" stroke-linejoin="round"/></svg>STORIES</li>
        <li><svg viewBox="0 0 14 14"><path d="M1 7.5 L5 11.5 L13 2.5" fill="none" stroke="#de6d31" stroke-width="2.4" stroke-linecap="round" stroke-linejoin="round"/></svg>MOVEMENT</li>
      </ul>
    </section>

    <div class="free-tag"><span>FREE!</span></div>

    <div class="reserve-bar">Reservations required
      <svg viewBox="0 0 20 20"><path d="M9 8 L9 18 L11.5 15.5 L13.5 19 L15 18.2 L13 14.8 L16.5 14.5 Z" fill="#fff"/><path d="M6 6 L3.5 3.5 M9 4.5 L9 1 M4.5 9 L1 9 M12 6 L14 4" stroke="#fff" stroke-width="1.4" stroke-linecap="round"/></svg>
    </div>

    <p class="visit">Visit <strong>larkandlantern.example</strong> for details.</p>

    <div class="address-band">
      <svg class="band" viewBox="0 0 850 56" preserveAspectRatio="none"><path d="M390 0 H850 V56 H373 Q366 20 390 0 Z" fill="#83912a"/></svg>
      <p class="address">
        <svg viewBox="0 0 18 24"><path d="M9 0 C4 0 0 4 0 9 C0 15 9 24 9 24 C9 24 18 15 18 9 C18 4 14 0 9 0 Z" fill="#fff"/><circle cx="9" cy="9" r="3.5" fill="#83912a"/></svg>
        387 E. 61st Avenue - San Mateo CA 94471
      </p>
    </div>
  </main>
</body>
</html>
```